Premium Personal Brand — Facebook Banner (Used Across All Platforms)

Update — Additional Color Direction
In addition to the dark charcoal/slate direction already described, I'm also interested in seeing variants with:
Dark navy blue — Deep, authoritative, intelligence-community feel. Same textured/matte treatment, not flat or bright.
Warm charcoal with steel blue accent — Keep the dark base but introduce a subtle steel blue gradient, accent line, or tonal shift. Sophisticated, modern, adds dimension without adding color noise.
Both should maintain the same premium, restrained, architectural feel described in the original brief. No bright blues, no corporate PowerPoint energy — think midnight, think depth, think weight.
Everything else in the brief remains the same.
I am building a premium personal brand as an executive advisor to founders ($5M+ revenue).
This contest is Facebook-banner–focused, but the design must represent a visual system that will be reused across:
- LinkedIn
- YouTube
I- nstagram
- X (Twitter)
- Website hero sections and other brand touchpoints
Think of the Facebook banner as the primary expression of the brand — not a one-off graphic.
This project is about discovering a high-end visual style and brand feel, not decoration.
What to design
Please submit one cohesive visual system, shown primarily as:
- Facebook banner (primary focus)
The same design language should clearly translate to all platforms listed above.
Designers are responsible for using the current recommended dimensions for each platform.
Quick clarification on background direction:
Backgrounds should have depth and texture, not flat color fields. Avoid pure white, light grey, or solid black backgrounds. Think matte, architectural materials — stone, graphite, concrete, steel — not blank canvases. Subtle tonal variation is encouraged. Obvious gradients or decorative patterns are not.
Text to use
Primary Headline:
- Your Business Is Too Valuable To Be Run On Hope.
Subheadline:
- You didn’t build a business to become its prisoner.
Name:
Milo Verant
The headline should be the dominant visual element.
Logo note (important)
My personal logo is currently being finalized.
For this contest:
- Use a simple “MV” monogram placeholder
- Clean, bold, geometric sans-serif
- Do not design a logo
- The winning design must allow an easy logo swap later.
Headshot note (important)
- Please do not include a headshot in the banner design.
- Most platforms display a circular profile image separately.
- The banner should stand on its own using typography, layout, and tone only.
- Design the banner assuming the profile photo will sit nearby, not inside the banner.
Style direction
The design should feel:
- Premium
- Calm
- Confident
- Restrained
- High-trust
- Dark, neutral backgrounds are preferred.
- Fewer elements are better than more.
Think:
- Owner-level advisor
- Private equity / boardroom tone
- Industrial, Modern, Minimalist, Elite, Architectural, not decorative
What to avoid
Please do not submit designs that feel:
- Promotional, hype-driven, or salesy
- Like a coach, guru, or agency
- Bright, colorful, or gradient-heavy
- Busy or over-designed
- Based on stock photos
- No motivational speaker energy.
Reaction test
- If someone sees this banner on Facebook (or later on LinkedIn, YouTube, etc.), the reaction should be:
“That person is serious. I’d trust them with important decisions.”
Final note
- I am not looking for many variations.
- I am looking for one strong visual direction you believe in.
Simple beats clever.
- Restraint beats decoration.

```html
<!DOCTYPE html>
<html lang="en">
<head>
<meta charset="UTF-8">
<title>Milo Verant — Banner</title>
<link href="https://fonts.googleapis.com/css2?family=Outfit:wght@600&family=Arimo:wght@400&display=swap" rel="stylesheet">
<style>
  :root {
    --slate-deep: #121212;
    --slate-mid: #262626;
    --slate-light: #353535;
    --headline: #e6e6e6;
    --body-text: #ececec;
    --rule: #d9d9d9;
    --crack: #5a5a5a;
  }
  html, body {
    margin: 0;
    padding: 0;
    width: 1200px;
    height: 400px;
    overflow: hidden;
    background: var(--slate-deep);
  }
  .banner {
    position: relative;
    width: 1200px;
    height: 400px;
    overflow: hidden;
    background:
      radial-gradient(ellipse 45% 60% at 20% 20%, rgba(255,255,255,0.06), transparent 70%),
      radial-gradient(ellipse 40% 55% at 80% 45%, rgba(255,255,255,0.05), transparent 70%),
      linear-gradient(170deg, var(--slate-mid) 0%, var(--slate-deep) 60%, #181818 100%);
  }
  .banner__texture {
    position: absolute;
    inset: 0;
  }
  .banner__headline {
    position: absolute;
    left: 77px;
    top: 72px;
    margin: 0;
    font-family: "Outfit", sans-serif;
    font-weight: 600;
    font-size: 57px;
    line-height: 70px;
    letter-spacing: 0.5px;
    text-transform: uppercase;
    white-space: nowrap;
    color: var(--headline);
  }
  .banner__rule {
    position: absolute;
    left: 76px;
    top: 236px;
    width: 786px;
    height: 2px;
    background: var(--rule);
  }
  .banner__subheadline {
    position: absolute;
    left: 77px;
    top: 256px;
    margin: 0;
    font-family: "Arimo", sans-serif;
    font-weight: 400;
    font-size: 35.5px;
    line-height: 36px;
    white-space: nowrap;
    color: var(--body-text);
  }
  .banner__signature {
    position: absolute;
    right: 87px;
    top: 312px;
    margin: 0;
    font-family: "Arimo", sans-serif;
    font-size: 25px;
    line-height: 30px;
    white-space: nowrap;
    color: var(--body-text);
  }
  .banner__signature-dash {
    margin-right: 10px;
  }
</style>
</head>
<body>
  <section class="banner">
    <svg class="banner__texture" width="1200" height="400" viewBox="0 0 1200 400" role="img" aria-label="Dark slate stone surface with faint natural cracks">
      <defs>
        <filter id="stoneGrain" x="0" y="0" width="100%" height="100%">
          <feTurbulence type="fractalNoise" baseFrequency="0.9" numOctaves="3" seed="4" result="fine"/>
          <feColorMatrix in="fine" type="saturate" values="0"/>
        </filter>
        <filter id="stoneMottle" x="0" y="0" width="100%" height="100%">
          <feTurbulence type="fractalNoise" baseFrequency="0.008 0.02" numOctaves="4" seed="11"/>
          <feColorMatrix type="saturate" values="0"/>
        </filter>
        <linearGradient id="stoneShade" x1="0" y1="0" x2="0" y2="1">
          <stop offset="0" stop-color="#000" stop-opacity="0"/>
          <stop offset="1" stop-color="#000" stop-opacity="0.3"/>
        </linearGradient>
      </defs>
      <rect width="1200" height="400" filter="url(#stoneMottle)" opacity="0.12"/>
      <rect width="1200" height="400" filter="url(#stoneGrain)" opacity="0.07"/>
      <g fill="none" stroke="var(--crack)" stroke-width="1" stroke-linecap="round" opacity="0.45">
        <path d="M585 130 C640 120 700 118 760 112 C800 108 830 100 870 88"/>
        <path d="M760 112 C780 150 790 190 820 215 C850 240 900 250 960 290"/>
        <path d="M1030 60 C1040 110 1020 160 1000 200 C985 235 1000 270 1040 300"/>
        <path d="M700 360 C740 330 790 310 840 300"/>
        <path d="M1100 20 C1120 60 1150 90 1190 110"/>
      </g>
      <rect width="1200" height="400" fill="url(#stoneShade)"/>
    </svg>

    <h1 class="banner__headline">Your business is too valuable<br>to be run on hope</h1>
    <div class="banner__rule"></div>
    <p class="banner__subheadline">You didn’t build a business to become its prisoner</p>
    <p class="banner__signature"><span class="banner__signature-dash">-</span>Milo Verant</p>
  </section>
</body>
</html>
```